Business card design needed for a security services business.

We provide a wide range of security services from guard personnel to electronic systems.

Industry/Entity Type

Security Industry

Contact Information for Business Card

Brent Holloway, Owner Office: 780.555.0148; Cell: 780.555.0193 Email: brent@norcrestwatchgroup.example; Address 20487 163 St Edmonton, AB T5X 2K8

Colors
0054AA
0677BA
7BADD7
CADEEF
E8F1F8

Requirements
Nice to have
• On the back of the card I would like to possible list the services I provide: Guards Mobiles Live Video Surveillance Access Intrusion

```html
<!DOCTYPE html>
<html lang="en">
<head>
<meta charset="utf-8">
<title>Norcrest Watch Group — Business Card</title>
<link href="https://fonts.googleapis.com/css2?family=Poppins:wght@400;600;700&display=swap" rel="stylesheet">
<style>
  :root {
    --page-bg: #1a1a1a;
    --card-front: #121212;
    --card-back: #676767;
    --brand-blue: #0677ba;
    --band-blue: #0a72c4;
    --text-white: #ffffff;
    --divider: #8f8f8f;
  }
  * { margin: 0; padding: 0; box-sizing: border-box; }
  html, body {
    width: 1200px;
    height: 900px;
    overflow: hidden;
    background: var(--page-bg);
    font-family: "Poppins", sans-serif;
  }
  .stage {
    width: 1200px;
    height: 900px;
    display: flex;
    flex-direction: column;
    align-items: center;
    justify-content: center;
    gap: 40px;
  }
  .card {
    position: relative;
    width: 630px;
    height: 360px;
    overflow: hidden;
  }
  .card::after {
    content: "";
    position: absolute;
    left: 0; right: 0; bottom: 0;
    height: 12px;
    background: var(--band-blue);
  }

  /* Front */
  .card--front { background: var(--card-front); }
  .brand {
    position: absolute;
    top: 110px;
    left: 0; right: 0;
    display: flex;
    justify-content: center;
    align-items: center;
    gap: 12px;
  }
  .brand__mark {
    width: 18px;
    height: 18px;
    background: var(--brand-blue);
  }
  .brand__name {
    color: var(--brand-blue);
    font-weight: 600;
    font-size: 30px;
    letter-spacing: 1px;
    text-transform: uppercase;
  }
  .services {
    position: absolute;
    top: 250px;
    left: 0; right: 0;
    text-align: center;
    color: var(--brand-blue);
    font-size: 13px;
    line-height: 1.5;
    letter-spacing: 0.6px;
    text-transform: uppercase;
  }

  /* Back */
  .card--back { background: var(--card-back); color: var(--text-white); }
  .identity {
    position: absolute;
    top: 100px;
    left: 40px;
    width: 290px;
    text-align: right;
  }
  .identity__name {
    font-weight: 700;
    font-size: 26px;
    letter-spacing: 0.3px;
    text-transform: uppercase;
    line-height: 1.1;
  }
  .identity__role {
    font-size: 14px;
    text-transform: uppercase;
    margin-top: 4px;
  }
  .divider {
    position: absolute;
    top: 110px;
    left: 348px;
    width: 1px;
    height: 72px;
    background: var(--divider);
  }
  .address {
    position: absolute;
    top: 122px;
    left: 368px;
    font-size: 15px;
    line-height: 1.4;
  }
  .contact {
    position: absolute;
    top: 258px;
    left: 40px;
    font-size: 15px;
    letter-spacing: 0.2px;
  }
</style>
</head>
<body>
  <main class="stage">
    <section class="card card--front" aria-label="Card front">
      <div class="brand">
        <span class="brand__mark"></span>
        <span class="brand__name">Norcrest Watch Group</span>
      </div>
      <p class="services">Guards , Mobiles Live<br>Video Surveillance,&nbsp; Access Intrusion</p>
    </section>

    <section class="card card--back" aria-label="Card back">
      <div class="identity">
        <h1 class="identity__name">Brent Holloway</h1>
        <p class="identity__role">Owner</p>
      </div>
      <span class="divider"></span>
      <p class="address">20487 163 St Edmonton<br>AB T5X 2K8</p>
      <p class="contact">780.555.0148,&nbsp; 780.555.0193 , brent@norcrestwatchgroup.example</p>
    </section>
  </main>
</body>
</html>
```